San Francisco Pet Care Non Profit

Business Card Design for non profit organization.
We are a Street Pet Outreach who supports and attends to pets whose owners are homeless. Thanks for your help and creativity.

Industry/Entity Type

Non Profit

Contact Information for Business Card

Miriam Loxley
President
2817 Harrow Street, #516
San Francisco, CA 94187
phone: 415-782-3946
fax: 415-718-4053
miriam@warmpawvan.org
website: warmpawvan.org
facebook: WarmPawVan

Font styles to use
Serif
Sans Serif

Colors

Designer to choose colors to be used in the design.

Requirements
Must have
• above details and attached logo

```html
<!DOCTYPE html>
<html lang="en">
<head>
<meta charset="utf-8">
<title>Harbor Tails – Business Card</title>
<link rel="stylesheet" href="https://fonts.googleapis.com/css2?family=Exo+2:wght@300;400;600;700&display=swap">
<style>
  :root {
    --sky: #35a7e0;
    --sky-soft: #e6f2fa;
    --ink: #121314;
    --paper: #ffffff;
    --stage: #e4e5e7;
    --text: #1d1f22;
  }
  * { box-sizing: border-box; margin: 0; padding: 0; }
  html, body { width: 1200px; height: 800px; overflow: hidden; }
  body {
    background: var(--stage);
    font-family: "Exo 2", sans-serif;
    display: flex;
    align-items: center;
    justify-content: center;
    gap: 40px;
  }
  .card {
    position: relative;
    width: 540px;
    height: 309px;
    background: var(--paper);
    overflow: hidden;
    box-shadow: 0 6px 18px rgba(0,0,0,.18);
  }
  .card-bands { position: absolute; inset: 0; }

  /* front */
  .front-brand {
    position: absolute;
    left: 0; right: 0; top: 118px;
    display: flex; align-items: center; justify-content: center; gap: 18px;
    color: var(--paper);
  }
  .brand-dot {
    width: 56px; height: 56px; border-radius: 50%;
    border: 3px solid currentColor;
    flex: none;
  }
  .brand-text { display: flex; flex-direction: column; }
  .brand-name { font-size: 44px; font-weight: 700; line-height: 1; letter-spacing: .5px; }
  .brand-tagline { font-size: 16px; font-weight: 700; margin-top: 6px; letter-spacing: .5px; }

  /* back */
  .back-watermark {
    position: absolute;
    left: -20px; top: 70px;
    width: 210px; height: 210px; border-radius: 50%;
    border: 6px solid var(--sky-soft);
  }
  .back-brand {
    position: absolute;
    right: 34px; top: 34px;
    display: flex; align-items: center; gap: 12px;
  }
  .back-brand .brand-dot { width: 42px; height: 42px; border: 2px solid var(--sky); }
  .back-brand .brand-name { font-size: 34px; color: var(--sky); }
  .back-brand .brand-tagline { font-size: 13px; color: var(--ink); margin-top: 4px; }

  .holder {
    position: absolute;
    left: 24px; top: 148px;
    color: var(--paper);
    display: flex; align-items: baseline; gap: 10px;
  }
  .holder-name { font-size: 22px; font-weight: 700; letter-spacing: 1px; text-transform: uppercase; }
  .holder-role { font-size: 12px; font-weight: 600; letter-spacing: 1px; text-transform: uppercase; }

  .contact-list {
    position: absolute;
    list-style: none;
    font-size: 14px; font-weight: 300; color: var(--text);
  }
  .contact-list li { display: flex; align-items: flex-start; gap: 9px; margin-bottom: 7px; line-height: 1.25; }
  .contact-left { left: 26px; top: 206px; }
  .contact-right { left: 300px; top: 206px; }
  .icon {
    width: 20px; height: 20px; border-radius: 50%;
    background: var(--sky);
    flex: none;
    display: flex; align-items: center; justify-content: center;
  }
  .icon svg { width: 12px; height: 12px; }
</style>
</head>
<body>

  <section class="card card-front" aria-label="Card front">
    <svg class="card-bands" viewBox="0 0 540 309" aria-hidden="true">
      <rect width="540" height="309" fill="var(--sky)"/>
      <polygon points="0,52 188,52 200,42 212,52 540,52 540,255 306,255 294,265 282,255 0,255" fill="var(--paper)"/>
      <polygon points="0,60 190,60 200,52 210,60 540,60 540,247 304,247 294,255 284,247 0,247" fill="var(--ink)"/>
    </svg>
    <div class="front-brand">
      <span class="brand-dot"></span>
      <div class="brand-text">
        <span class="brand-name">Harbor Tails</span>
        <span class="brand-tagline">Street Pet Outreach</span>
      </div>
    </div>
  </section>

  <section class="card card-back" aria-label="Card back">
    <span class="back-watermark" aria-hidden="true"></span>
    <svg class="card-bands" viewBox="0 0 540 309" aria-hidden="true">
      <polygon points="0,186 540,186 540,193 0,193" fill="var(--ink)"/>
      <polygon points="0,138 410,138 420,130 430,138 540,138 540,186 0,186" fill="var(--sky)"/>
      <polygon points="38,193 58,193 48,202" fill="var(--ink)"/>
    </svg>

    <div class="back-brand">
      <span class="brand-dot"></span>
      <div class="brand-text">
        <span class="brand-name">Harbor Tails</span>
        <span class="brand-tagline">Street Pet Outreach</span>
      </div>
    </div>

    <div class="holder">
      <span class="holder-name">Miriam Loxley</span>
      <span class="holder-role">President</span>
    </div>

    <ul class="contact-list contact-left">
      <li>
        <span class="icon"><svg viewBox="0 0 24 24"><path fill="#fff" d="M6.6 10.8a15 15 0 0 0 6.6 6.6l2.2-2.2a1 1 0 0 1 1-.25 11.4 11.4 0 0 0 3.6.57 1 1 0 0 1 1 1V20a1 1 0 0 1-1 1A17 17 0 0 1 3 4a1 1 0 0 1 1-1h3.5a1 1 0 0 1 1 1c0 1.25.2 2.45.57 3.57a1 1 0 0 1-.25 1z"/></svg></span>
        415-782-3946
      </li>
      <li>
        <span class="icon"><svg viewBox="0 0 24 24"><path fill="#fff" d="M7 3h10v5H7zM4 9h16a1 1 0 0 1 1 1v7h-4v4H7v-4H3v-7a1 1 0 0 1 1-1zm5 6v4h6v-4z"/></svg></span>
        415-718-4053
      </li>
      <li>
        <span class="icon"><svg viewBox="0 0 24 24"><path fill="#fff" d="M12 2a7 7 0 0 0-7 7c0 5 7 13 7 13s7-8 7-13a7 7 0 0 0-7-7zm0 9.5A2.5 2.5 0 1 1 12 6.5a2.5 2.5 0 0 1 0 5z"/></svg></span>
        <span>2817 Harrow Street, #516<br>San Francisco, CA 94187</span>
      </li>
    </ul>

    <ul class="contact-list contact-right">
      <li>
        <span class="icon"><svg viewBox="0 0 24 24"><path fill="#fff" d="M3 5h18v14H3zm2 2v.5l7 5 7-5V7l-7 5z"/></svg></span>
        miriam@warmpawvan.org
      </li>
      <li>
        <span class="icon"><svg viewBox="0 0 24 24"><circle cx="12" cy="12" r="8.5" fill="none" stroke="#fff" stroke-width="2"/><path d="M3.5 12h17M12 3.5c-4 4.5-4 12.5 0 17M12 3.5c4 4.5 4 12.5 0 17" fill="none" stroke="#fff" stroke-width="1.6"/></svg></span>
        warmpawvan.org
      </li>
      <li>
        <span class="icon"></span>
        WarmPawVan
      </li>
    </ul>
  </section>

</body>
</html>
```